tanjak dine in

we are thai, malaysian, vietnamese restaurant. Southeast Asia, we love antique, classic, cozy ambiance, and illustrate arts form.
I would like to design lunch,dinner and limited take out menu a classic, elegant, and fun menu, healthy earthy, feels like in southeast asia

attachment are some example files that you can review it
this is us www.lovetanjak.com
would like to follow http://www.kirinlanternhall.com 's style

restaurants that around the coner,
www.saltpebble.com
http://www.brovanelle.com
http://www.rosatorvans.com
http://www.copperkettleeatery.com

Target Market(s)

neighbourhood, HSC students, modern and hip

Font styles to use
Other font styles liked:
• fonts that match my old menu

Colors
faa54b
fece3e
ebf1f7
acd037
ec2027
000000

Requirements
Nice to have
• insider tips: Don't waste money on lousy food = instant regret
• Keep Calm Curry On

```html
<!DOCTYPE html>
<html lang="en">
<head>
<meta charset="utf-8">
<title>Tanjak — Lunch Combo</title>
<link href="https://fonts.googleapis.com/css2?family=Arvo:wght@400;700&family=Source+Sans+3:wght@400;600&family=PT+Sans:wght@400;700&family=PT+Sans+Narrow&family=Kaushan+Script&display=swap" rel="stylesheet">
<style>
:root{
  --wood-dark:#2b1a0f;
  --wood:#4a2e1a;
  --paper:#d8c398;
  --paper-light:#e6d6b0;
  --band:rgba(240,214,150,.55);
  --strip:rgba(255,250,235,.35);
  --red:#8a1717;
  --banner:#7d1113;
  --gold:#efc03a;
  --ink:#2a1a10;
  --chilli:#c8201f;
  --leaf:#2f7a2a;
  --white:#ffffff;
}
*{margin:0;padding:0;box-sizing:border-box}
html,body{width:1200px;height:1016px;overflow:hidden;background:var(--wood-dark)}
.menu{position:relative;width:1200px;height:1016px;overflow:hidden;
  background:linear-gradient(180deg,var(--wood) 0%,var(--wood-dark) 100%);
  font-family:"PT Sans",sans-serif;color:var(--ink)}
.paper{position:absolute;left:0;top:142px;width:1200px;height:738px;
  background:linear-gradient(100deg,var(--paper) 0%,var(--paper-light) 45%,var(--paper) 100%);
  clip-path:polygon(0 3%,8% 1%,17% 3.5%,28% 0,40% 2.5%,52% 0.5%,63% 3%,75% 1%,86% 3%,95% 0.5%,100% 2.5%,100% 97%,92% 99.5%,80% 97.5%,68% 100%,55% 97.5%,43% 99.5%,30% 97%,18% 99.5%,8% 97.5%,0 99.5%)}
.band{position:absolute;left:0;width:1200px;background:var(--band)}
.strip{position:absolute;left:0;width:1200px;background:var(--strip)}
.brand{position:absolute;left:30px;top:22px;font-family:"Arvo",serif;font-weight:700;font-size:62px;color:var(--white);line-height:1}
.tagline{position:absolute;left:428px;top:62px;font-family:"Arvo",serif;font-weight:700;font-size:18px;letter-spacing:.5px;color:var(--gold)}
.hours{position:absolute;left:1048px;top:25px;width:106px;height:106px;border-radius:50%;background:var(--gold);
  display:flex;flex-direction:column;align-items:center;justify-content:center;font-family:"Arvo",serif;font-weight:700;color:var(--ink);line-height:1}
.hours b{font-size:23px}.hours small{font-size:14px;font-weight:400;margin:3px 0}
.combo-banner{position:absolute;left:44px;top:188px;width:316px;height:50px;background:var(--banner);
  font-family:"Arvo",serif;font-size:26px;letter-spacing:1px;color:var(--gold);display:flex;align-items:center;justify-content:center}
.combo-info{position:absolute;left:394px;top:195px;font-family:"Arvo",serif;color:var(--ink)}
.combo-info .lead{font-size:19px;letter-spacing:.3px}
.combo-info .rule{font-size:14px;font-weight:700;margin-top:1px}
.section{position:absolute;left:54px;font-family:"Arvo",serif;font-weight:700;font-size:19px;letter-spacing:1px;color:var(--ink)}
.section span{letter-spacing:.5px}
.divider{position:absolute;top:300px;height:544px;border-left:1px dashed rgba(42,26,16,.6)}
.item{position:absolute;left:var(--x);top:var(--y);width:340px}
.item h3{font-family:"Source Sans 3",sans-serif;font-weight:600;font-size:20px;color:var(--red);line-height:1.1}
.item p{font-family:"PT Sans Narrow",sans-serif;font-size:14px;line-height:15.5px;color:var(--red);margin-top:2px}
.icon{display:inline-block;vertical-align:middle;margin-left:4px}
.dessert h3{font-size:20px}
.deliver{position:absolute;left:40px;top:922px;color:var(--white)}
.deliver h4{font-family:"Arvo",serif;font-weight:700;font-size:24px;color:var(--gold);line-height:1}
.deliver p{font-size:17px;line-height:18px;margin-top:8px}
.contact{position:absolute;right:442px;top:922px;text-align:right;color:var(--white)}
.contact .phone{font-family:"Arvo",serif;font-weight:700;font-size:24px;color:var(--gold);line-height:1}
.contact p{font-family:"Arvo",serif;font-size:16px;line-height:18px;margin-top:8px}
.contact p+p{margin-top:0}
.specials{position:absolute;left:806px;top:910px;width:364px;height:102px;background:var(--gold);color:var(--ink);text-align:center}
.specials .ask{font-family:"Arvo",serif;font-size:23px;padding-left:60px;margin-top:14px;line-height:1}
.specials .daily{font-family:"Kaushan Script",cursive;font-size:42px;line-height:1}
</style>
</head>
<body>
<main class="menu">
  <div class="paper" role="img" aria-label="Aged paper texture panel"></div>
  <div class="strip" style="top:266px;height:32px"></div>
  <div class="band" style="top:298px;height:174px"></div>
  <div class="strip" style="top:474px;height:34px"></div>
  <div class="band" style="top:510px;height:245px"></div>
  <div class="strip" style="top:757px;height:30px"></div>
  <div class="band" style="top:787px;height:57px"></div>

  <header>
    <div class="brand">Tanjak</div>
    <div class="tagline">MALAYSIAN &amp; THAI STREET FOOD</div>
    <div class="hours"><b>12pm</b><small>till</small><b>3pm</b></div>
  </header>

  <div class="combo-banner">LUNCH COMBO</div>
  <div class="combo-info">
    <div class="lead">Choose your choice of cuisine for only 12</div>
    <div class="rule">Choice of 1 (One) Appetizer + 1 (One) Entree + 1 (One) Dessert</div>
  </div>

  <svg width="0" height="0" style="position:absolute">
    <defs>
      <symbol id="chilli" viewBox="0 0 24 16"><path d="M20 3c2 0 3 1 3 2-2 0-3 1-4 3-3 5-10 7-17 7 6-2 10-6 12-10 1-2 3-2 6-2z" fill="#c8201f"/><path d="M19 3l2-3" stroke="#2f7a2a" stroke-width="2"/></symbol>
      <symbol id="leaf" viewBox="0 0 36 16"><path d="M2 8C8 1 22 0 34 6 26 15 10 16 2 8z" fill="#2f7a2a"/><path d="M4 8h28" stroke="#bfe0a0" stroke-width="1"/></symbol>
    </defs>
  </svg>

  <div class="section" style="top:274px">APPETIZER <span>(choose 1)</span></div>
  <div class="section" style="top:486px">ENTREE <span>(choose 1)</span></div>
  <div class="section" style="top:764px">DESSERT &amp; TREATS <span>(choose 1)</span></div>

  <div class="divider" style="left:420px"></div>
  <div class="divider" style="left:804px"></div>

  <!-- Appetizers -->
  <div class="item" style="--x:52px;--y:307px"><h3>Thai Boneless Fried Chicken Wings</h3><p>Coconut milk, pandan leaves, Tumeric, Shaoxing<br>cooking wine hot &amp; spicy glazed <svg class="icon" width="22" height="14"><use href="#chilli"/></svg></p></div>
  <div class="item" style="--x:52px;--y:382px"><h3>Kaffil-lime lemongrass<br>tumeric mussles</h3><p>Basil Lemongrass wok saute Mussles hand pounded<br>chilli lemongrass paste <svg class="icon" width="22" height="14"><use href="#chilli"/></svg></p></div>
  <div class="item" style="--x:452px;--y:307px"><h3>BBQ Char Siu Bun</h3><p>Roasted chicken or pork, Thai dark soy sauce,<br>citrus- honey glazed, cucumber pickles,<br>tomatoes, toasted sesame seeds</p></div>
  <div class="item" style="--x:452px;--y:397px"><h3>Plump's Dumplings</h3><p>Pork, chive, smoked chilli oil, peanut sauce</p></div>
  <div class="item" style="--x:850px;--y:307px"><h3>Roti Canai Melora</h3><p>Handmade Malaysian crispy and fluffy roti<br>dough, vegeterian dal dip <svg class="icon" width="32" height="14"><use href="#leaf"/></svg></p></div>
  <div class="item" style="--x:850px;--y:391px"><h3>Malay Spring Rolls</h3><p>Jicama, carrot, cilantro, sweet chili dipping sauce<br><svg class="icon" style="margin-left:0" width="22" height="14"><use href="#chilli"/></svg><svg class="icon" width="32" height="14"><use href="#leaf"/></svg></p></div>

  <!-- Entrees -->
  <div class="item" style="--x:52px;--y:523px"><h3>Pad Thai</h3><p>Sweet radish, egg, chives, beansprout, roasted<br>peanut, fresh lime, paprika <svg class="icon" width="32" height="14"><use href="#leaf"/></svg></p></div>
  <div class="item" style="--x:52px;--y:595px"><h3>Pad Kee Mao</h3><p>Fresh flat Chow Fun, tomatoes, Birdseye chilli,<br>onion, bell pepper, basil leaves <svg class="icon" width="22" height="14"><use href="#chilli"/></svg><svg class="icon" width="32" height="14"><use href="#leaf"/></svg></p></div>
  <div class="item" style="--x:52px;--y:670px"><h3>Ka Prao Basil Sauce</h3><p>Garlic, Thai chilli, bell pepper, onion, egg, fresh<br>Thai basil leaves <svg class="icon" width="22" height="14"><use href="#chilli"/></svg><svg class="icon" width="32" height="14"><use href="#leaf"/></svg></p></div>
  <div class="item" style="--x:452px;--y:523px"><h3>Classic Pho Bò Huế *</h3><p>beef meat ball, Vietnamese spices, cardamom<br>pods, black peppercorn, chopped coriander leaf</p></div>
  <div class="item" style="--x:452px;--y:595px"><h3>Crab Meat Fried Rice*</h3><p>Scallion, ginger, egg, crab meat, Thai seafood<br>dipping soy sauce</p></div>
  <div class="item" style="--x:452px;--y:672px"><h3>Cashew Smoked Chilli</h3><p>Bell pepper, cashew nuts, onion, Thai sweet chilli paste<br><svg class="icon" style="margin-left:0" width="22" height="14"><use href="#chilli"/></svg><svg class="icon" width="32" height="14"><use href="#leaf"/></svg></p></div>
  <div class="item" style="--x:845px;--y:523px"><h3>Curry Laksa*</h3><p>Mix seafood, lemongrass chicken stock, egg,<br>fried tofu, mint leaves, scallion <svg class="icon" width="22" height="14"><use href="#chilli"/></svg></p></div>
  <div class="item" style="--x:845px;--y:595px"><h3>Vegeterian Curry Clay Pot</h3><p>cabbage, potatoes, long beans, carrots, fried tofu,<br>tomatoes, eggplant, fresh chilli <svg class="icon" width="22" height="14"><use href="#chilli"/></svg><svg class="icon" width="32" height="14"><use href="#leaf"/></svg></p></div>
  <div class="item" style="--x:845px;--y:670px"><h3>Thai Green Curry</h3><p>Fresh pounded Green chilli paste, lemongrass,<br>bamboo strips, Thai eggplant, bell pepper, long<br>beans, fresh basil <svg class="icon" width="22" height="14"><use href="#chilli"/></svg><svg class="icon" width="32" height="14"><use href="#leaf"/></svg></p></div>

  <!-- Desserts -->
  <div class="item dessert" style="--x:52px;--y:795px"><h3>Mango Sticky Rice Coconut Cream</h3></div>
  <div class="item dessert" style="--x:455px;--y:795px"><h3>Coconut Jam &amp; Butter Toast</h3></div>
  <div class="item dessert" style="--x:850px;--y:795px"><h3>China Town Style Coffee with<br>Cinnamon Cookies</h3></div>

  <footer>
    <div class="deliver"><h4>WE DELIVER</h4><p>Follow us on Chirpline, Friendboard<br>or Spotlog for locations &amp; hours</p></div>
    <div class="contact"><div class="phone">646-555-0172</div><p>@LOVETANJAK</p><p>www.lovetanjak.com</p></div>
    <div class="specials"><div class="ask">Ask about our</div><div class="daily">daily specials!</div></div>
  </footer>
</main>
</body>
</html>
```